Business Card Design Project - KLB

I am looking for a more sophisticated card design for my company,
"The Kestrel Bureau"

We are a consultancy focused on strategy and change in Associations and professional organisations.

I am a lawyer and psychologist with a PhD and so am looking for something that communicates seriousness and credibility but also quirky creative solutions for strategic problems, which is my field of speciality.

I am looking for something that is quietly spoken, rather than loud colours ('credible' and 'creative' are the two adjectives that I think of as competing here).

I particularly like an embossed card style - heavy white card with plain white or white and black or white and grey text.

The key logo image for the company is a question mark and I am open to suggestions and ideas on design.

I have attached a file that includes a couple of styles that have caught my eye and my thoughts on them. Hopefully they communicate what I'm looking for.
Updates

Thank you for all the great suggestions and designs.

I really appreciated the effort and creative energy you put into your designs. I have now closed the project after selecting a design and advising the successful designer of the card that I am happy with.

Regards

Target Market(s)

Organisations (CEO's and Boards), Governments, Legal professionals, Membership Associations and aspiring professionals.

Industry/Entity Type

Lawyer

Requirements
Must have
• The key logo element is a question mark (?) and this needs to be incorporated.

Embossed style - cut outs or other design ideas interest me too.

The attached file has a number of sample ideas and comments on each one that I like.
Should not have
• I like crisp, modern fonts (Myriads etc...) and do not like embellished fonts or Times etc...

```html
<!DOCTYPE html>
<html lang="en">
<head>
<meta charset="utf-8">
<title>The Kestrel Bureau – Business Card Concepts</title>
<link rel="stylesheet" href="https://fonts.googleapis.com/css2?family=Jost:wght@400;700&display=swap">
<style>
  :root{
    --slate:#7f889b;
    --navy:#15213f;
    --red:#ad1d2e;
    --grey:#a8a8a8;
    --pale:#c9c9c9;
    --white:#ffffff;
    --black:#000000;
  }
  *{margin:0;padding:0;box-sizing:border-box}
  html,body{width:1200px;height:900px;overflow:hidden;background:var(--slate);font-family:"Jost",sans-serif}
  .sheet{position:relative;width:1200px;height:900px}
  .card{position:absolute;width:567px;height:290px;overflow:hidden}
  .card svg{position:absolute;left:0;top:0;width:567px;height:290px}
  .front{left:16px}
  .back{left:602px}
  .row-1{top:5px}.row-2{top:298px}.row-3{top:592px}

  /* front colourways */
  .front--navy{background:var(--white);--banner:var(--navy);--title:var(--white);--rule:var(--pale);--rule2:var(--pale);--wing:var(--navy);--band:var(--navy);--stripe:var(--white);--box:var(--grey);--edge:var(--white);--name:var(--red)}
  .front--black{background:var(--black);--banner:var(--white);--title:var(--grey);--rule:var(--grey);--rule2:var(--grey);--wing:var(--white);--band:var(--red);--stripe:var(--white);--box:var(--grey);--edge:var(--black);--name:var(--navy)}
  .front--grey{background:var(--grey);--banner:var(--white);--title:var(--navy);--rule:var(--grey);--rule2:var(--navy);--wing:var(--white);--band:var(--white);--stripe:var(--navy);--box:var(--red);--edge:var(--grey);--name:var(--white)}

  .banner{fill:var(--banner)}
  .rule{stroke:var(--rule);stroke-width:1.5}
  .rule-dot{fill:var(--rule)}
  .rule--lower{stroke:var(--rule2)}
  .rule-dot--lower{fill:var(--rule2)}
  .wing{fill:var(--wing)}
  .band{fill:var(--band)}
  .stripe{fill:var(--stripe)}

  .company{position:absolute;left:8px;top:8px;width:551px;height:68px;display:flex;align-items:center;justify-content:center;
    font-weight:700;font-size:27px;letter-spacing:-0.3px;color:var(--title);text-transform:uppercase}
  .details{position:absolute;left:77px;top:94px;width:412px;height:190px;background:var(--box);border:3px solid var(--edge);color:var(--white)}
  .details__head{height:43px;border-bottom:3px solid var(--edge);text-align:center;padding-top:4px}
  .details__name{font-weight:700;font-size:20px;line-height:21px;color:var(--name);text-transform:uppercase}
  .details__role{font-weight:400;font-size:12px;line-height:12px;text-transform:uppercase}
  .details__list{padding:6px 0 0 12px}
  .details__label{font-weight:700;font-size:9px;line-height:10px;text-transform:uppercase}
  .details__value{font-weight:400;font-size:14.5px;line-height:15px;margin-bottom:2px}

  /* back colourways */
  .back--white{background:var(--white);--band:var(--navy);--mark:var(--grey);--dot:var(--red)}
  .back--black{background:var(--black);--band:var(--red);--mark:var(--white);--dot:var(--white)}
  .back--grey{background:var(--grey);--band:var(--white);--mark:var(--navy);--dot:var(--red)}
  .back__band{position:absolute;left:0;top:183px;width:567px;height:72px;background:var(--band)}
  .brand{position:absolute;left:18px;top:96px;display:flex;gap:14px}
  .brand__name{font-weight:700;font-size:58px;line-height:58px;color:var(--mark);text-transform:uppercase;letter-spacing:-1px}
  .brand__dot{width:78px;height:78px;border-radius:50%;background:var(--dot)}
</style>
</head>
<body>
<main class="sheet">

  <section class="card front front--navy row-1">
    <svg viewBox="0 0 567 290" aria-hidden="true">
      <rect class="band" x="0" y="182" width="567" height="73"/>
      <rect class="stripe" x="0" y="223" width="567" height="5"/>
      <rect class="banner" x="8" y="8" width="551" height="68"/>
      <line class="rule" x1="58" y1="67" x2="508" y2="67"/><circle class="rule-dot" cx="58" cy="67" r="2.5"/><circle class="rule-dot" cx="508" cy="67" r="2.5"/>
      <line class="rule rule--lower" x1="122" y1="86" x2="444" y2="86"/><circle class="rule-dot rule-dot--lower" cx="122" cy="86" r="2.5"/><circle class="rule-dot rule-dot--lower" cx="444" cy="86" r="2.5"/>
      <polygon class="wing" points="12,80 118,80 74,142 12,142"/>
      <polygon class="wing" points="555,80 449,80 493,142 555,142"/>
    </svg>
    <div class="company">The Kestrel Bureau</div>
    <div class="details">
      <div class="details__head"><p class="details__name">Dr Marcus Ellery</p><p class="details__role">Director</p></div>
      <div class="details__list">
        <p class="details__label">Post</p><p class="details__value">P.O. Box 4180, Alder Heights<br>Sydney, Australia</p>
        <p class="details__label">Mobile</p><p class="details__value">0491 570 156</p>
        <p class="details__label">Work</p><p class="details__value">(02) 5550 1234</p>
        <p class="details__label">E-mail</p><p class="details__value">marcus@kestrelbureau.com.au</p>
      </div>
    </div>
  </section>

  <section class="card front front--black row-2">
    <svg viewBox="0 0 567 290" aria-hidden="true">
      <rect class="band" x="0" y="183" width="567" height="72"/>
      <rect class="stripe" x="0" y="223" width="567" height="5"/>
      <rect class="banner" x="8" y="8" width="551" height="68"/>
      <line class="rule" x1="58" y1="67" x2="508" y2="67"/><circle class="rule-dot" cx="58" cy="67" r="2.5"/><circle class="rule-dot" cx="508" cy="67" r="2.5"/>
      <line class="rule rule--lower" x1="122" y1="86" x2="444" y2="86"/><circle class="rule-dot rule-dot--lower" cx="122" cy="86" r="2.5"/><circle class="rule-dot rule-dot--lower" cx="444" cy="86" r="2.5"/>
      <polygon class="wing" points="12,80 118,80 74,142 12,142"/>
      <polygon class="wing" points="555,80 449,80 493,142 555,142"/>
    </svg>
    <div class="company">The Kestrel Bureau</div>
    <div class="details">
      <div class="details__head"><p class="details__name">Dr Marcus Ellery</p><p class="details__role">Director</p></div>
      <div class="details__list">
        <p class="details__label">Post</p><p class="details__value">P.O. Box 4180, Alder Heights<br>Sydney, Australia</p>
        <p class="details__label">Mobile</p><p class="details__value">0491 570 156</p>
        <p class="details__label">Work</p><p class="details__value">(02) 5550 1234</p>
        <p class="details__label">E-mail</p><p class="details__value">marcus@kestrelbureau.com.au</p>
      </div>
    </div>
  </section>

  <section class="card front front--grey row-3">
    <svg viewBox="0 0 567 290" aria-hidden="true">
      <rect class="band" x="0" y="183" width="567" height="73"/>
      <rect class="stripe" x="0" y="222" width="567" height="4"/>
      <rect class="banner" x="8" y="8" width="551" height="68"/>
      <line class="rule" x1="58" y1="67" x2="508" y2="67"/><circle class="rule-dot" cx="58" cy="67" r="2.5"/><circle class="rule-dot" cx="508" cy="67" r="2.5"/>
      <line class="rule rule--lower" x1="122" y1="86" x2="444" y2="86"/><circle class="rule-dot rule-dot--lower" cx="122" cy="86" r="2.5"/><circle class="rule-dot rule-dot--lower" cx="444" cy="86" r="2.5"/>
      <polygon class="wing" points="12,80 118,80 74,142 12,142"/>
      <polygon class="wing" points="555,80 449,80 493,142 555,142"/>
    </svg>
    <div class="company">The Kestrel Bureau</div>
    <div class="details">
      <div class="details__head"><p class="details__name">Dr Marcus Ellery</p><p class="details__role">Director</p></div>
      <div class="details__list">
        <p class="details__label">Post</p><p class="details__value">P.O. Box 4180, Alder Heights<br>Sydney, Australia</p>
        <p class="details__label">Mobile</p><p class="details__value">0491 570 156</p>
        <p class="details__label">Work</p><p class="details__value">(02) 5550 1234</p>
        <p class="details__label">E-mail</p><p class="details__value">marcus@kestrelbureau.com.au</p>
      </div>
    </div>
  </section>

  <section class="card back back--white row-1">
    <div class="back__band"></div>
    <div class="brand"><p class="brand__name">Kestrel<br>Bureau</p><span class="brand__dot"></span></div>
  </section>

  <section class="card back back--black row-2">
    <div class="back__band"></div>
    <div class="brand"><p class="brand__name">Kestrel<br>Bureau</p><span class="brand__dot"></span></div>
  </section>

  <section class="card back back--grey row-3">
    <div class="back__band"></div>
    <div class="brand"><p class="brand__name">Kestrel<br>Bureau</p><span class="brand__dot"></span></div>
  </section>

</main>
</body>
</html>
```